Need a stunning home page for Car rental company

For a client, I need a slick and sumber home page design. It is a small, local car rental company, with a handful of cars available for rent.
Selling points: affordable lease, availability, always clean cars
The design should be:
- flat and modern
- no, or very few animations/sliders
- CTA: booking form for renting a car.
- 3 featured cars with images and facts (see website) with button to read more about the car.
- fullscreen background video can be an option
- main colour: #efba01
The site is under construction here:
http://tavnumobil.kessvira.no/
Delivery requirements:
I need a layered & well organised PSD file delivered.

```html
<!DOCTYPE html>
<html lang="no">
<head>
<meta charset="utf-8">
<title>Tavnu Bilutleie</title>
<link rel="stylesheet" href="https://fonts.googleapis.com/css2?family=PT+Sans+Narrow:wght@400;700&family=PT+Sans:ital@1&display=swap">
<style>
  :root{
    --brand:#efba01;
    --brand-soft:#f6be3a;
    --ink:#2b2b2b;
    --muted:#6d6d6d;
    --dark:#3d3d3d;
    --panel:#e9e9e9;
    --white:#ffffff;
  }
  *{margin:0;padding:0;box-sizing:border-box}
  html,body{width:1200px;height:1164px;overflow:hidden;background:var(--white)}
  body{position:relative;font-family:"PT Sans Narrow",sans-serif;color:var(--ink)}
  .abs{position:absolute}

  /* header */
  .site-header{position:absolute;left:0;top:0;width:1200px;height:102px;background:var(--white)}
  .brand-name{left:167px;top:30px;font-size:30px;font-weight:700;color:#7a7a7a;letter-spacing:1px;text-transform:uppercase}
  .nav-tab{top:0;height:90px;background:linear-gradient(90deg,#e7e7e7,#fff 60%);}
  .nav-link{top:31px;font-size:17px;color:#111}
  .nav-link.active{color:var(--brand)}
  .flag{top:37px;width:16px;height:11px}

  /* hero */
  .hero{left:0;top:102px;width:1200px;height:474px;background:linear-gradient(100deg,#c9cdd0 0%,#8f8a86 25%,#b9453f 38%,#5e5a55 52%,#c7b79b 72%,#a9936c 100%)}
  .hero-band{left:0;top:102px;width:1200px;height:70px;background:rgba(70,70,70,.75)}
  .call-label{left:708px;top:124px;font-family:"PT Sans",sans-serif;font-style:normal;font-size:17px;color:var(--white)}
  .call-number{left:864px;top:110px;font-size:40px;font-weight:700;color:var(--brand-soft)}
  .hero-title{left:636px;top:236px;font-size:32px;font-weight:700;color:var(--brand-soft)}
  .hero-sub{left:636px;top:270px;font-size:21px;font-weight:700;color:var(--white)}
  .hero-text{left:639px;top:323px;width:380px;font-size:15.5px;line-height:17px;color:var(--white)}
  .hero-cta{left:636px;top:432px;width:183px;height:48px;background:var(--brand-soft);color:var(--white);font-size:21px;text-align:center;line-height:48px}

  /* cars */
  .car-divider{top:594px;width:1px;height:238px;background:#d4d4d4}
  .car{top:594px;width:300px;height:240px}
  .car-title{position:absolute;left:1px;top:0;font-size:28px;font-weight:700;color:var(--brand-soft)}
  .car-photo{position:absolute;left:2px;top:43px;width:100px;height:85px;background:linear-gradient(180deg,#e9eef2,#b8c0c6)}
  .spec{position:absolute;left:125px;top:38px;font-size:12.5px;line-height:17px}
  .spec dt{position:absolute;left:0;width:100px;font-weight:700;color:#555}
  .spec dd{position:absolute;left:102px;color:#777}
  .price-label{position:absolute;left:2px;top:143px;font-size:15px;color:var(--muted)}
  .price{position:absolute;left:1px;top:158px;font-size:32px;font-weight:700;color:var(--brand-soft)}
  .rent-btn{position:absolute;left:0;top:203px;width:140px;height:33px;background:linear-gradient(180deg,#555,#2f2f2f);color:var(--white);font-size:16px;font-weight:700;text-align:center;line-height:33px}

  /* lower band */
  .lower{left:0;top:857px;width:1200px;height:276px;background:var(--panel)}
  .lower-line{left:190px;top:852px;width:470px;height:3px;background:linear-gradient(90deg,transparent,#fff 30%,#fff 70%,transparent)}
  .quote-badge{left:372px;top:844px;width:37px;height:37px;border-radius:50%;background:var(--white);color:#444;font-family:Georgia,serif;font-size:28px;font-weight:700;text-align:center;line-height:44px}
  .avatar{left:190px;top:915px;width:90px;height:93px;border:4px solid var(--white);border-radius:4px;box-shadow:0 2px 5px rgba(0,0,0,.25);background:linear-gradient(160deg,#d8e6f2,#9fb6cc)}
  .quote{left:320px;top:924px;width:345px;font-family:"PT Sans",sans-serif;font-style:italic;font-size:12.5px;line-height:17px;color:#555}
  .author{left:198px;top:1038px;font-size:17px;color:#555}
  .author-role{left:215px;top:1061px;font-size:9px;color:var(--brand)}
  .dot{top:1041px;width:10px;height:10px;border-radius:50%;background:#cfcfcf}
  .social-label{left:469px;top:1037px;font-size:12px;color:#555}
  .social{top:1031px;width:24px;height:24px;border-radius:5px;background:#8a8a8a}
  .vsep{left:709px;top:888px;width:0;height:205px;border-left:1px dotted #777}
  .nl-title{left:783px;top:900px;font-size:18px;font-weight:700;color:var(--brand-soft)}
  .nl-sub{left:782px;top:922px;font-size:16px;color:#777}
  .nl-input{left:772px;top:961px;width:239px;height:34px;background:var(--white);border:1px solid #ddd}
  .nl-note{left:783px;top:1010px;width:230px;font-size:10.5px;line-height:13px;font-style:italic;color:#888}
  .nl-btn{left:783px;top:1058px;width:139px;height:33px;background:var(--brand-soft);color:var(--white);font-size:15px;font-weight:700;text-align:center;line-height:33px}

  .site-footer{left:0;top:1133px;width:1200px;height:31px;background:var(--dark);color:#ddd;font-size:10px}
  .site-footer .links{position:absolute;left:170px;top:10px}
  .site-footer .copy{position:absolute;right:164px;top:10px}
</style>
</head>
<body>
  <header class="site-header">
    <div class="abs brand-name">Tavnu Bilutleie</div>
    <div class="abs nav-tab" style="left:557px;width:132px"></div>
    <div class="abs nav-tab" style="left:689px;width:113px"></div>
    <div class="abs nav-tab" style="left:802px;width:125px"></div>
    <div class="abs nav-tab" style="left:927px;width:72px"></div>
    <a class="abs nav-link active" style="left:496px">Hjem</a>
    <a class="abs nav-link" style="left:591px">Bilparken vår</a>
    <a class="abs nav-link" style="left:720px">Tjenester</a>
    <a class="abs nav-link" style="left:838px">Kontakt Oss</a>
    <svg class="abs flag" style="left:976px" viewBox="0 0 22 16"><rect width="22" height="16" fill="#ba0c2f"/><rect x="6" width="4" height="16" fill="#fff"/><rect y="6" width="22" height="4" fill="#fff"/><rect x="7" width="2" height="16" fill="#00205b"/><rect y="7" width="22" height="2" fill="#00205b"/></svg>
    <svg class="abs flag" style="left:1006px" viewBox="0 0 22 16"><rect width="22" height="16" fill="#012169"/><path d="M0 0L22 16M22 0L0 16" stroke="#fff" stroke-width="3"/><path d="M0 0L22 16M22 0L0 16" stroke="#c8102e" stroke-width="1"/><rect x="9" width="4" height="16" fill="#fff"/><rect y="6" width="22" height="4" fill="#fff"/><rect x="10" width="2" height="16" fill="#c8102e"/><rect y="7" width="22" height="2" fill="#c8102e"/></svg>
  </header>

  <section>
    <div class="abs hero" role="img" aria-label="Photo of a smiling man in a checked shirt holding up car keys from the window of a white van"></div>
    <div class="abs hero-band"></div>
    <div class="abs call-label">Spørsmål? Ring oss</div>
    <div class="abs call-number">47 11 29 03</div>
    <h1 class="abs hero-title">Velkommen til Tavnu Bilutleie</h1>
    <div class="abs hero-sub">Tavnuvik</div>
    <p class="abs hero-text">Tavnu bilutleie er en bilpark på Tavnuvik, og leier ut varebiler og personbiler til deg som trenger en ekstrabil til flytting, ferie, bytur eller hva det måtte være. Vi er uslåelige på service, og mest sannsynlig også på pris. Og du kan stole på at bilen du får fra oss er både ren og pen!</p>
    <a class="abs hero-cta">RENT A CAR NOW</a>
  </section>

  <section>
    <div class="abs car-divider" style="left:444px"></div>
    <div class="abs car-divider" style="left:757px"></div>

    <article class="abs car" style="left:151px">
      <h2 class="car-title">Varebilen</h2>
      <div class="car-photo" role="img" aria-label="Photo of a white van"></div>
      <dl class="spec">
        <dt style="top:0">Biltype</dt><dd style="top:0">Varebil</dd>
        <dt style="top:17px">Maks.</dt><dd style="top:17px">pers.2</dd>
        <dt style="top:34px">Ant.</dt><dd style="top:34px">dører5</dd>
        <dt style="top:51px">Min. sjåføralder</dt><dd style="top:51px">21</dd>
        <dt style="top:68px">Girtype</dt><dd style="top:68px">Manuell</dd>
        <dt style="top:85px">Klimaanlegg?</dt><dd style="top:85px">Ja</dd>
        <dt style="top:102px">Ubegrenset km?</dt><dd style="top:102px">Nei</dd>
      </dl>
      <div class="price-label">Pris per døgn</div>
      <div class="price">kr 600</div>
      <a class="rent-btn">RENT THIS CAR</a>
    </article>

    <article class="abs car" style="left:468px">
      <h2 class="car-title">Varebilen</h2>
      <div class="car-photo" role="img" aria-label="Photo of a white van"></div>
      <dl class="spec">
        <dt style="top:0">Biltype</dt><dd style="top:0">Varebil</dd>
        <dt style="top:17px">Maks.</dt><dd style="top:17px">pers.2</dd>
        <dt style="top:34px">Ant.</dt><dd style="top:34px">dører5</dd>
        <dt style="top:51px">Min. sjåføralder</dt><dd style="top:51px">21</dd>
        <dt style="top:68px">Girtype</dt><dd style="top:68px">Manuell</dd>
        <dt style="top:85px">Klimaanlegg?</dt><dd style="top:85px">Ja</dd>
        <dt style="top:102px">Ubegrenset km?</dt><dd style="top:102px">Nei</dd>
      </dl>
      <div class="price-label">Pris per døgn</div>
      <div class="price">kr 600</div>
      <a class="rent-btn">RENT THIS CAR</a>
    </article>

    <article class="abs car" style="left:785px">
      <h2 class="car-title">Varebilen</h2>
      <div class="car-photo" role="img" aria-label="Photo of a white van"></div>
      <dl class="spec">
        <dt style="top:0">Biltype</dt><dd style="top:0">Varebil</dd>
        <dt style="top:17px">Maks.</dt><dd style="top:17px">pers.2</dd>
        <dt style="top:34px">Ant.</dt><dd style="top:34px">dører5</dd>
        <dt style="top:51px">Min. sjåføralder</dt><dd style="top:51px">21</dd>
        <dt style="top:68px">Girtype</dt><dd style="top:68px">Manuell</dd>
        <dt style="top:85px">Klimaanlegg?</dt><dd style="top:85px">Ja</dd>
        <dt style="top:102px">Ubegrenset km?</dt><dd style="top:102px">Nei</dd>
      </dl>
      <div class="price-label">Pris per døgn</div>
      <div class="price">kr 600</div>
      <a class="rent-btn">RENT THIS CAR</a>
    </article>
  </section>

  <section>
    <div class="abs lower"></div>
    <div class="abs lower-line"></div>
    <div class="abs quote-badge">“</div>
    <div class="abs avatar" role="img" aria-label="Portrait photo of a smiling grey-haired customer"></div>
    <blockquote class="abs quote">Sed ut perspiciatis unde omnis iste natus sit voluptatem accusantium doloremque laudantium, totam rem aperiam, eaque ipsa quae ab illo inventore veritatis et quasi . Sed ut perspiciatis unde omnis iste natus sit voluptatem accusantium.</blockquote>
    <div class="abs author">- Per Eksempel</div>
    <div class="abs author-role">Lorem Ipsum Elit</div>
    <span class="abs dot" style="left:320px"></span>
    <span class="abs dot" style="left:334px"></span>
    <span class="abs dot" style="left:348px"></span>
    <div class="abs social-label">Get Social</div>
    <span class="abs social" style="left:524px"></span>
    <span class="abs social" style="left:550px"></span>
    <span class="abs social" style="left:576px"></span>
    <span class="abs social" style="left:602px"></span>
    <span class="abs social" style="left:628px"></span>
    <div class="abs vsep"></div>
    <h3 class="abs nl-title">SUBSCRIBE TO OUR NEWSLETTER</h3>
    <div class="abs nl-sub">Lorem Ipsum Consectetur Adipiscing Elit</div>
    <div class="abs nl-input"></div>
    <p class="abs nl-note">Sed ut perspiciatis unde omnis iste natus sit voluptatem accusantium. Sed ut perspiciatis unde omnis.</p>
    <a class="abs nl-btn">SUBSCRIBE</a>
  </section>

  <footer class="abs site-footer">
    <span class="links">Terms of Use | Privacy Policy</span>
    <span class="copy">Copyright Tavnu Bilutleie © 2014. All Rights Reserved.</span>
  </footer>
</body>
</html>
```